Wageline Associates Business Card Design

We need a business card designed around our new logo. The business card should be modern in design & should communicate success, confidence, power, sophistication. The target market is young business professionals. This is for a human resource & payroll outsourcing business.

```html
<!DOCTYPE html>
<html lang="en">
<head>
<meta charset="utf-8">
<title>Wageline Associates Business Card</title>
<link rel="stylesheet" href="https://fonts.googleapis.com/css2?family=Questrial&display=swap">
<style>
  :root{
    --stage:#3b3e43;
    --ink:#0b0b0c;
    --paper:#ffffff;
    --accent:#e3141f;
    --soft:#d9d9d9;
  }
  *{box-sizing:border-box;margin:0;padding:0}
  html,body{width:1200px;height:900px;overflow:hidden;background:var(--stage)}
  body{font-family:"Questrial",sans-serif;position:relative}
  .card{position:absolute;left:280px;width:640px;height:380px;border-radius:34px;overflow:hidden;box-shadow:0 12px 28px rgba(0,0,0,.35)}
  .card--front{top:45px;background:var(--paper)}
  .card--back{top:475px;background:var(--ink)}
  .card__wave{position:absolute;inset:0;width:100%;height:100%}
  .brand{position:absolute;display:flex;align-items:center;gap:10px;font-weight:400;letter-spacing:.5px;z-index:1}
  .brand__dot{width:12px;height:12px;border-radius:50%;background:var(--accent)}
  .card--front .brand{left:60px;top:22px;color:var(--ink);font-size:28px}
  .card--back .brand{left:50%;top:132px;transform:translateX(-50%);color:var(--paper);font-size:42px;white-space:nowrap}
  .address{position:absolute;left:40px;top:205px;color:var(--paper);font-size:13px;line-height:1.5;z-index:1}
  .person{position:absolute;right:48px;top:226px;text-align:right;color:var(--paper);z-index:1}
  .person__name{color:var(--accent);font-size:24px;font-weight:400;line-height:1.1}
  .person__role{font-size:15px;margin-top:2px}
  .contacts{list-style:none;margin-top:8px;font-size:12.5px;line-height:1.4}
  .contacts li{display:flex;justify-content:flex-end;align-items:center;gap:8px}
  .contacts svg{width:11px;height:11px;fill:var(--accent)}
  .web{position:absolute;left:50%;bottom:92px;transform:translateX(-50%);color:var(--soft);font-size:16px;letter-spacing:4px}
</style>
</head>
<body>
  <section class="card card--front">
    <svg class="card__wave" viewBox="0 0 640 380" preserveAspectRatio="none" aria-hidden="true">
      <path d="M0,70 C60,75 100,140 240,158 C400,175 560,168 640,190" fill="none" stroke="var(--ink)" stroke-width="6"/>
      <path d="M0,82 C60,87 100,152 240,170 C400,187 560,180 640,202" fill="none" stroke="var(--accent)" stroke-width="5"/>
      <path d="M0,92 C60,97 100,162 240,180 C400,197 560,190 640,212 L640,380 L0,380 Z" fill="var(--ink)"/>
    </svg>
    <div class="brand"><span class="brand__dot"></span><span>Wageline Associates</span></div>
    <p class="address">Harlow Junction<br>Eastfield Marlow, 1620</p>
    <div class="person">
      <h1 class="person__name">Marten Kole</h1>
      <p class="person__role">General Manager</p>
      <ul class="contacts">
        <li>02 5550 1870 <svg viewBox="0 0 12 12"><path d="M3 1l2 2-1 1.5c.6 1.4 1.7 2.5 3 3L8.5 6.5l2 2-1.3 1.8C5.5 10 2 6.5 1.7 2.3z"/></svg></li>
        <li>0411 555 246 <svg viewBox="0 0 12 12"><path d="M3.5 0h5a1 1 0 0 1 1 1v10a1 1 0 0 1-1 1h-5a1 1 0 0 1-1-1V1a1 1 0 0 1 1-1zm.5 1.5v8h4v-8z"/></svg></li>
        <li>contact@wageline.com.au <svg viewBox="0 0 12 12"><path d="M0 2h12v8H0zm1 1v.4l5 3 5-3V3z"/></svg></li>
        <li>www.wageline.com <svg viewBox="0 0 12 12"><circle cx="6" cy="6" r="5.5"/></svg></li>
      </ul>
    </div>
  </section>

  <section class="card card--back">
    <div class="brand"><span class="brand__dot"></span><span>Wageline Associates</span></div>
    <p class="web">www.wageline.com</p>
  </section>
</body>
</html>
```